Harborview House and Shelter for Servicemembers needs an invitation for our Gala

The size is 15 x 7 but will need to fold to 5.25 x 7.25 (an A7 envelope) The invitation can appear vertical or horizontally. This is a 4 color, 2 sided invitation.
The design inspiration should come from the event logo. The logo can appear long or can be stacked.
The text needed and the logo for the event are attached.
The Harborview House and Shelter for Servicemembers, is hosting it's 14th Annual Stand Together Always Gala on November 2nd at the Quayside Exchange Pavilion. We are looking for a new design concept for our invitation and program book materials using an existing logo.
The concept can use images, however if the designer chooses to use an image, they must incorporate all military branches and both men and women. The final design should communicate elegance and be reflective of the organization and event logo. We will take into consideration a four, two or one color design. Lastly, the HHSS and event logos can appear next to each other or side by side.
Our mission: The Harborview House for Unhoused Servicemembers was founded in 1989 and is a private not-for-profit organization. The Center is one of the nation’s largest private resources for Veterans of every era who may be facing challenges and are at-risk of homelessness. Our experienced professionals provide the tools and direct Veterans to resources that enable successful independent living and meaningful employment.
Here's a link to our website for reference:
hhss-shelter.org

```html
<!DOCTYPE html>
<html lang="en">
<head>
<meta charset="utf-8">
<title>Stand Together Always Gala – Invitation</title>
<link rel="stylesheet" href="https://fonts.googleapis.com/css2?family=Montserrat:wght@500&family=Oswald:wght@400;500&family=Pinyon+Script&display=swap">
<style>
  :root {
    --paper: #f1f1f1;
    --navy: #2b3a8c;
    --navy-deep: #1b2a6e;
    --flag-blue: #25399a;
    --flag-red: #b3202c;
    --logo-ink: #1f2a57;
  }
  html, body {
    margin: 0;
    padding: 0;
    width: 1200px;
    height: 600px;
    overflow: hidden;
    background: var(--paper);
  }
  .invitation {
    position: relative;
    width: 1200px;
    height: 600px;
    background: var(--paper);
    overflow: hidden;
  }
  .invitation__art {
    position: absolute;
    inset: 0;
    width: 1200px;
    height: 600px;
    display: block;
  }
  .title-annual {
    font-family: "Montserrat", sans-serif;
    font-weight: 500;
    fill: var(--navy);
  }
  .title-event {
    font-family: "Oswald", sans-serif;
    font-weight: 400;
    fill: var(--flag-red);
  }
  .title-date {
    font-family: "Oswald", sans-serif;
    font-weight: 400;
    fill: var(--navy);
  }
  .title-venue {
    font-family: "Oswald", sans-serif;
    font-weight: 400;
    fill: var(--navy);
  }
  .title-gala {
    font-family: "Pinyon Script", cursive;
    fill: var(--navy);
  }
  .host-name {
    font-family: "Oswald", sans-serif;
    font-weight: 400;
    fill: var(--logo-ink);
  }
</style>
</head>
<body>
<main class="invitation">
  <svg class="invitation__art" viewBox="0 0 1200 600" xmlns="http://www.w3.org/2000/svg">
    <defs>
      <linearGradient id="bannerTone" x1="0" y1="0" x2="1" y2="0">
        <stop offset="0" stop-color="var(--flag-red)"/>
        <stop offset="0.45" stop-color="#8a2a5a"/>
        <stop offset="1" stop-color="var(--flag-blue)"/>
      </linearGradient>
    </defs>

    <!-- top banner area -->
    <path class="top-banner" role="img" aria-label="Waving red, white and blue flag with stars"
          fill="url(#bannerTone)"
          d="M0,0 H1200 V240 C1120,280 1060,300 1000,294 C850,282 720,190 480,188 C300,186 120,260 0,444 Z"/>

    <!-- row of stars above the title -->
    <rect class="star-row" role="img" aria-label="Row of eight small stars"
          x="328" y="240" width="308" height="18" rx="4" fill="var(--navy)" opacity="0.85"/>

    <!-- event title -->
    <text class="title-annual" x="302" y="330" font-size="50" textLength="358" lengthAdjust="spacingAndGlyphs">14TH ANNUAL</text>
    <text class="title-event" x="246" y="408" font-size="84" textLength="492" lengthAdjust="spacingAndGlyphs">STAND TOGETHER ALWAYS</text>
    <text class="title-gala" x="744" y="436" font-size="190" textLength="250" lengthAdjust="spacingAndGlyphs">gala</text>
    <text class="title-date" x="346" y="466" font-size="46" textLength="264" lengthAdjust="spacingAndGlyphs">NOVEMBER 2ND</text>
    <text class="title-venue" x="349" y="499" font-size="24" textLength="257" lengthAdjust="spacingAndGlyphs">QUAYSIDE EXCHANGE PAVILION</text>

    <!-- underline swooshes -->
    <path class="swoosh swoosh--blue" fill="var(--navy-deep)"
          d="M198,526 C400,516 600,514 740,528 C600,522 400,524 198,530 Z"/>
    <path class="swoosh swoosh--red" fill="var(--flag-red)"
          d="M198,546 C400,540 600,540 736,552 C600,546 400,548 198,551 Z"/>

    <!-- host organisation -->
    <text class="host-name" x="898" y="544" font-size="20" textLength="251" lengthAdjust="spacingAndGlyphs">HARBORVIEW HOUSE</text>
    <text class="host-name" x="914" y="560" font-size="11" textLength="220" lengthAdjust="spacingAndGlyphs">FOR UNHOUSED SERVICEMEMBERS</text>
  </svg>
</main>
</body>
</html>
```